2016 QMB Tournament Trail Schedule

I need a flyer designed for our 2016 QMB Trail. We are a Texas based bass tournament trail. We are announcing $10K guaranteed for first at all 6 regular season events and $20K guaranteed for first at our 2 day fall championship. On the flyer we'd also like to show our schedule.

Jan 30 - Lake LBJ
Feb 27 - Canyon Lake
April 2 - Lake Travis
April 30 - Belton Lake
May 21 - Lake Buchanan
June 18 - Lake Waco

Fall Championship - TBD

Adult teams $200 entry includes big bass pot
Youth/adult teams $150 entry includes big bass pot

The flyer needs to be bass fishing related and we can provide pictures if you have ideas. We do not want it to look redneck'ish though. Our website is qmb1.net and would prefer a similar look. Lot's of black, red, and grey.

We have attached the QMB logo and we would also like Norvane and Dolkira logos incorporated. Norvane boats (which are are owned by Dolkira motors) is our title sponsor

Target Market(s)

Our anglers

Font styles to use
Other font styles liked:
• Something Cool

Colors
474747
ec1f27
000000
dbdbdb

Requirements
Must have
• Tournament dates and locations entry costs, payout guarantees
• QMB logo, Norvane Logo, Dolkira Logo
Nice to have
• go to www.qmb1.net to see our website, this should give you a feel for our style
• or qmbforum.net another site we operate

```html
<!DOCTYPE html>
<html lang="en">
<head>
<meta charset="utf-8">
<title>QMB Bass Tournament Trail 2016</title>
<link rel="stylesheet" href="https://fonts.googleapis.com/css2?family=Anton&family=Oswald:wght@500;700&display=swap">
<style>
  :root {
    --black: #000000;
    --red: #ec1f27;
    --blue: #1f3c8f;
    --white: #ffffff;
    --grey: #dbdbdb;
    --charcoal: #474747;
  }
  * { margin: 0; padding: 0; box-sizing: border-box; }
  html, body { width: 849px; height: 1200px; overflow: hidden; background: var(--black); }
  .flyer {
    position: relative;
    width: 849px; height: 1200px;
    background: var(--black);
    color: var(--white);
    font-family: "Oswald", sans-serif;
    overflow: hidden;
  }
  .brand-name {
    position: absolute; left: 40px; top: 22px;
    display: flex; align-items: center; gap: 18px;
    font-family: "Anton", sans-serif;
    font-size: 112px; line-height: 1.1; color: var(--white);
    letter-spacing: 4px;
  }
  .brand-mark { width: 40px; height: 40px; background: var(--red); }
  .brand-tagline {
    position: absolute; left: 100px; top: 176px;
    font-weight: 700; font-size: 26px; line-height: 1; letter-spacing: 3px; color: var(--white);
  }
  .brand-series {
    position: absolute; left: 40px; top: 208px;
    font-family: "Anton", sans-serif; font-size: 40px; line-height: 1.1; letter-spacing: 1px;
    text-transform: uppercase;
  }
  .brand-series .accent { color: var(--red); }
  .bass-art {
    position: absolute; right: 20px; top: 10px; width: 280px; height: 240px;
    border-radius: 45% 55% 40% 60%;
    background: radial-gradient(ellipse at 40% 45%, #9a9a9a 0%, #5a5a5a 55%, rgba(0,0,0,0) 75%);
  }
  .prize-band {
    position: absolute; left: 0; width: 849px;
    display: flex; align-items: center; justify-content: center; gap: 26px;
  }
  .prize-regular {
    top: 268px; height: 108px; background: var(--blue);
    border-top: 4px solid var(--white); border-bottom: 4px solid var(--white);
  }
  .prize-championship {
    top: 392px; height: 138px; background: var(--white); color: var(--red);
  }
  .prize-amount { font-family: "Anton", sans-serif; font-size: 104px; line-height: 1; }
  .prize-regular .prize-amount { color: var(--white); }
  .prize-detail {
    font-family: "Anton", sans-serif; font-size: 38px; line-height: 1.05;
    text-transform: uppercase; text-align: left;
  }
  .schedule {
    position: absolute; left: 40px; top: 552px; width: 770px;
    display: grid; grid-template-columns: 1fr 1fr; column-gap: 30px;
    font-weight: 700; font-size: 34px; line-height: 42px;
  }
  .championship-date {
    position: absolute; left: 0; top: 782px; width: 849px; text-align: center;
    font-family: "Anton", sans-serif; font-size: 42px; line-height: 1.1; color: var(--red); letter-spacing: 1px;
  }
  .entry-fees {
    position: absolute; left: 0; top: 834px; width: 849px; text-align: center;
    font-weight: 700; font-size: 30px; line-height: 40px;
  }
  .website {
    position: absolute; left: 0; top: 912px; width: 849px; text-align: center;
    font-family: "Anton", sans-serif; font-size: 100px; line-height: 1.2; color: var(--red); letter-spacing: 2px;
  }
  .sponsors {
    position: absolute; left: 0; top: 1110px; width: 849px; height: 70px;
    display: flex; justify-content: space-around; align-items: center;
  }
  .sponsor {
    display: flex; align-items: center; gap: 12px;
    font-family: "Anton", sans-serif; font-size: 40px; color: var(--white);
    text-transform: uppercase; letter-spacing: 2px;
  }
  .sponsor-dot { width: 30px; height: 30px; border-radius: 50%; background: var(--white); }
</style>
</head>
<body>
  <div class="flyer">
    <div class="brand-name"><span class="brand-mark"></span>QMB</div>
    <div class="brand-tagline">QUARRY MESA BASS</div>
    <div class="brand-series">Bass <span class="accent">Tournament</span> Trail</div>
    <div class="bass-art" role="img" aria-label="Illustration of a leaping largemouth bass"></div>

    <section class="prize-band prize-regular">
      <div class="prize-amount">$10K</div>
      <div class="prize-detail">Guaranteed for 1st<br>place at all events</div>
    </section>
    <section class="prize-band prize-championship">
      <div class="prize-amount">$20K</div>
      <div class="prize-detail">Guaranteed at our 2<br>day fall championship</div>
    </section>

    <section class="schedule">
      <div>Jan 30 - Lake LBJ</div>
      <div>April 30 - Belton Lake</div>
      <div>Feb 27 - Canyon Lake</div>
      <div>May 21 - Lake Buchanan</div>
      <div>April 2 - Lake Travis</div>
      <div>June 18 - Lake Waco</div>
    </section>

    <div class="championship-date">FALL CHAMPIONSHIP - TBD</div>
    <div class="entry-fees">
      <p>Adult teams $200 entry includes big bass pot</p>
      <p>Youth/adult teams $150 entry includes big bass pot</p>
    </div>

    <div class="website">www.qmb1.net</div>

    <footer class="sponsors">
      <div class="sponsor">Norvane</div>
      <div class="sponsor"><span class="sponsor-dot"></span>Dolkira</div>
    </footer>
  </div>
</body>
</html>
```